Amber Kite Foundation Inforgraphic

We are in need of an infographic layout to highlight facts for a medical foundation - the Amber Kite Foundation. We are a foundation dedicated to early detection and screening of pulmonary arterial hypertension, a deadly combination heart and lung disease We need a graphic that incorporates the following facts:

(1) Pulmonary Hypertension Symptoms: •Chest Pain
•Dizziness
•Shortness of Breath
•Fatigue
•Edema or swelling
•Cyanosis or skin discoloration

(2) Typically PH patients are consulted by 3 or more physicians before diagnosis

(3) PH patient’s generally incur 2.8 years between symptom onset and diagnosis via right heart catheterization

(4) Left untreated, the average life expectancy of a PAH patient is approximately 3 years from symptom onset

(5) No improvement has been achieved in early detection rates of PH since 1995

(6) 5 year survival rates are measured at 86% for PH patients diagnosed in early stages. 5 year survival rates for PH patients diagnosed late stages decrease to 50%

We want to incorporate these highlights into a fun and easy to follow infographic that can be transferred onto a large scale display banner.

We want to utilize our logo somewhere on the graphic. The logo file is attached. We also want to incorporate our slogan: Igniting the (ph)ight against pulmonary arterial hypertension through early detection and screening.

Thanks.

Industry/Entity Type

Medical

Colors
0555a3
3176b5
85acd3

Requirements
Must have
• Amber Kite Foundation Logo
• Dynamic display of graphics and figures to highlight statistics in the project discription

```html
<!DOCTYPE html>
<html lang="en">
<head>
<meta charset="utf-8">
<title>Amber Kite Foundation – Pulmonary Hypertension</title>
<link rel="stylesheet" href="https://fonts.googleapis.com/css2?family=Anton&family=Questrial&display=swap">
<style>
  :root {
    --brand-deep: #0555a3;
    --brand-mid: #3176b5;
    --brand-soft: #85acd3;
    --title-blue: #1a4fe0;
    --panel-main: #2f82ea;
    --fact-pale: #b9d4f4;
    --fact-mid: #6aa3ea;
    --fact-sky: #a6cdf4;
    --fact-light: #8fc3ef;
    --fact-blue: #6da6ef;
    --ink: #111;
    --paper: #ffffff;
  }
  * { margin: 0; padding: 0; box-sizing: border-box; }
  html, body { width: 1200px; height: 2329px; overflow: hidden; background: var(--paper); }
  .infographic { position: relative; width: 1200px; height: 2329px; font-family: "Questrial", sans-serif; }

  .brand { position: absolute; top: 110px; left: 0; width: 1200px; display: flex; justify-content: center; align-items: center; gap: 18px; }
  .brand-mark { width: 30px; height: 30px; background: var(--title-blue); }
  .brand-name { font-family: "Questrial", sans-serif; font-size: 46px; color: var(--title-blue); }

  .headline { position: absolute; left: 0; width: 1200px; text-align: center; font-family: "Anton", sans-serif; color: var(--title-blue); line-height: 1; transform-origin: center top; }
  .headline--one { top: 205px; font-size: 196px; letter-spacing: 4px; transform: scaleY(1.12); }
  .headline--two { top: 418px; font-size: 186px; letter-spacing: 2px; transform: scaleY(1.06); }

  .slogan { position: absolute; top: 628px; left: 0; width: 1200px; text-align: center; font-size: 30px; line-height: 1.35; color: #222; }

  .symptoms { position: absolute; left: 28px; top: 734px; width: 1097px; height: 836px; background: var(--panel-main); border-radius: 110px; overflow: hidden; }
  .organ-art { position: absolute; left: 560px; top: 150px; width: 360px; height: 680px; border-radius: 160px 160px 60px 60px; background: linear-gradient(180deg, rgba(20,60,140,0.10), rgba(20,60,140,0.22)); }
  .symptoms-title { position: absolute; left: 56px; top: 28px; font-family: "Anton", sans-serif; font-size: 150px; line-height: 1; color: var(--paper); -webkit-text-stroke: 6px var(--ink); paint-order: stroke fill; transform: rotate(-3deg) scaleY(1.05); text-shadow: 5px 6px 0 var(--ink); }
  .symptom-list { position: absolute; left: 0; top: 245px; width: 1097px; list-style: none; text-align: center; }
  .symptom-list li { font-size: 64px; line-height: 82px; color: var(--paper); -webkit-text-stroke: 5px var(--ink); paint-order: stroke fill; }

  .fact { position: absolute; display: flex; align-items: center; justify-content: center; text-align: center; border-radius: 48px; color: var(--paper); -webkit-text-stroke: 4px var(--ink); paint-order: stroke fill; padding: 10px 24px; }
  .fact--small { font-size: 34px; line-height: 1.08; }
  .fact--large { font-size: 42px; line-height: 1.12; }
  .fact--untreated { left: 28px; top: 1602px; width: 578px; height: 187px; background: var(--fact-pale); }
  .fact--detection { left: 28px; top: 1808px; width: 578px; height: 153px; background: var(--fact-mid); }
  .fact--survival { left: 28px; top: 1984px; width: 578px; height: 329px; background: var(--fact-sky); }
  .fact--physicians { left: 630px; top: 1602px; width: 495px; height: 296px; background: var(--fact-light); }
  .fact--delay { left: 630px; top: 1922px; width: 495px; height: 391px; background: var(--fact-blue); }
</style>
</head>
<body>
<main class="infographic">
  <header class="brand">
    <span class="brand-mark"></span>
    <span class="brand-name">Amber Kite Foundation</span>
  </header>

  <h1>
    <span class="headline headline--one">PULMONARY</span>
    <span class="headline headline--two">HYPERTENSION</span>
  </h1>
  <p class="slogan">Igniting the (ph)ight against pulmonary arterial hypertension<br>through early detection and screening.</p>

  <section class="symptoms">
    <div class="organ-art" role="img" aria-label="Line drawing of the lungs and windpipe"></div>
    <h2 class="symptoms-title">SYMPTOMS</h2>
    <ul class="symptom-list">
      <li>Chest Pain</li>
      <li>Dizziness</li>
      <li>Shortness of Breath</li>
      <li>Fatigue</li>
      <li>Edema or swelling</li>
      <li>Cyanosis or skin discoloration</li>
    </ul>
  </section>

  <p class="fact fact--small fact--untreated">Left untreated, the average life expectancy of a PAH patient is approximately 3 years from symptom onset</p>
  <p class="fact fact--small fact--detection">No improvement has been achieved in early detection rates of PH since 1995</p>
  <p class="fact fact--small fact--survival">5 year survival rates are measured at 86% for PH patients diagnosed in early stages.<br>5 year survival rates for PH patients diagnosed late stages decrease to 50%</p>
  <p class="fact fact--large fact--physicians">Typically PH patients are consulted by 3 or more physicians before diagnosis</p>
  <p class="fact fact--large fact--delay">PH patients generally incur 2.8 years between symptom onset and diagnosis via right heart catheterization</p>
</main>
</body>
</html>
```